Recruitment of Philippine Manpower for the UK market

I want a website for the UK market to attract businesses and companies to come to us for Philipine labour. We want an information site that gives all information on what we do and how we can recruit Philippine labour.
This is a recruitment site for companies to contact us with their requirements for skilled workers coming from the Philipines over to the UK to work.

Target Market(s)

Uk Companies and businesses who want Philipine skilled workers

Industry/Entity Type

REcruitment

Coding

Coded - Design and coding required

Number of Pages Required

5+ page

Font styles to use
Sans Serif

Colors
0054AA
0677BA
7BADD7
CADEEF
E8F1F8
0094D4
00A9DD
6FCCEA
C7EBF8
E9F6FB
EE7325
F08F49
F5BC92
FAE3D3
FDF4ED
EB3D1F
EC4F4E
F09395
F8D3D4
FCEDEE

Requirements
Must have
• Look professional and corperate with drop down menus for Home ,about, services,articles. training , contact us
Nice to have
• Look at Tovel recruitment- https://tovelrecruitment.example.co.uk/. This is my current site - https://www.brindlestaffing.example.com/
Should not have
• Cartoons or silly pictures , needs to be corperate looking

```html
<!DOCTYPE html>
<html lang="en">
<head>
<meta charset="utf-8">
<title>Brindle Staffing – Recruiting skilled Philippine workers</title>
<link href="https://fonts.googleapis.com/css2?family=Poppins:wght@400;500;600;700;800&display=swap" rel="stylesheet">
<style>
:root{
  --red:#eb3d1f;
  --orange:#ee7325;
  --ink:#222222;
  --text:#555555;
  --muted:#9a9a9a;
  --line:#d9d9d9;
  --footer:#2f2f2f;
  --white:#ffffff;
}
*{box-sizing:border-box;margin:0;padding:0}
html,body{width:1200px;height:4673px;overflow:hidden}
body{position:relative;background:var(--white);font-family:'Poppins',sans-serif;color:var(--ink)}
.abs{position:absolute}
a{color:inherit;text-decoration:none}

/* header */
.brand{left:90px;top:26px;display:flex;align-items:center;gap:10px;font-size:22px;font-weight:700;color:var(--red)}
.brand-mark{width:28px;height:28px;background:var(--red)}
.nav{left:595px;top:35px;display:flex;gap:22px;font-size:12.5px;font-weight:600;color:var(--ink)}
.nav .active{color:var(--red)}
.nav .drop::after{content:"";display:inline-block;width:5px;height:5px;border-right:1.5px solid currentColor;border-bottom:1.5px solid currentColor;transform:rotate(45deg);margin-left:5px;position:relative;top:-3px}

/* hero */
.hero-title{left:90px;top:148px;font-size:50px;line-height:64px;font-weight:700;width:680px;letter-spacing:-.5px}
.hl{color:var(--red)}
.stats{left:800px;top:210px;display:flex}
.stat{padding:0 38px 0 0;margin-right:30px;border-right:1px solid var(--line);height:78px}
.stat:last-child{border:0;margin:0;padding:0}
.stat b{display:block;font-size:25px;font-weight:500;color:var(--red);line-height:32px}
.stat span{display:block;font-size:11.5px;font-weight:600;line-height:16px;margin-top:6px}
.scroll-arrow{left:26px;top:488px}

.photo{background:linear-gradient(135deg,#2d4f8f 0%,#4a6fa8 35%,#b8571f 70%,#e07a2e 100%)}
.photo-engineer{left:89px;top:446px;width:1111px;height:415px}
.photo-engineer-low{left:89px;top:860px;width:616px;height:164px;background:linear-gradient(135deg,#2a4a8a,#4b6aa0 60%,#6f7f9a)}
.photo-weld{left:711px;top:861px;width:489px;height:584px;background:radial-gradient(circle at 35% 45%,#f2b25a 0%,#b5621f 25%,#3a2a20 60%,#111 100%)}
.play{left:918px;top:1121px;width:64px;height:64px;border:2px solid var(--white);border-radius:50%}
.outline-clip{overflow:hidden}
.outline{font-weight:800;color:transparent;-webkit-text-stroke:3px var(--white);white-space:nowrap;line-height:1}

/* intro */
.eyebrow{left:178px;top:1112px;font-size:12px;color:var(--muted);display:flex;align-items:center;gap:10px}
.eyebrow::before{content:"";width:32px;height:1px;background:var(--line)}
.intro-title{left:176px;top:1138px;font-size:36px;line-height:46px;font-weight:700}
.intro-text{left:178px;top:1240px;width:400px;font-size:13.5px;line-height:23px;color:var(--text)}
.more{font-size:12px;font-weight:700;border-bottom:1.5px solid var(--ink);padding-bottom:2px}

/* services */
.svc{top:1541px;width:236px;height:276px;color:var(--white);padding:52px 0 0 53px}
.svc.red{background:var(--red)}
.svc.orange{background:var(--orange)}
.svc h3{font-size:26px;line-height:31px;font-weight:600;margin-top:46px}
.svc .go{margin-top:18px}

/* training */
.photo-training{left:0;top:1967px;width:1200px;height:597px;background:linear-gradient(120deg,#1c2a44 0%,#2c4a86 40%,#c75a1f 65%,#2a4c94 100%)}

.lead{left:92px;top:2776px;font-size:37px;line-height:48px;font-weight:700;width:360px}
.row{left:515px;width:578px;display:flex;border-bottom:1px solid #9a9a9a}
.row:last-of-type{border:0}
.row h4{width:217px;font-size:21px;line-height:26px;font-weight:600;padding-top:28px}
.row p{width:356px;font-size:13px;line-height:23px;color:var(--text)}

/* articles */
.section-title{left:0;width:1200px;top:3210px;text-align:center;font-size:35px;font-weight:700}
.card{top:3278px;width:296px;height:370px;background:var(--white);box-shadow:0 4px 18px rgba(0,0,0,.08)}
.card-img{height:234px}
.card-body{padding:20px 28px}
.card-date{font-size:11px;font-weight:700;color:var(--red)}
.card-body h5{font-size:14.5px;font-weight:600;margin:10px 0 10px}
.card-body p{font-size:12.5px;line-height:18px;color:var(--text)}

/* footer */
.footer{left:0;top:4183px;width:1200px;height:490px;background:var(--footer)}
.faint{-webkit-text-stroke:2px #e8e8e8}
.map{left:221px;top:3856px;width:758px;height:386px;background:linear-gradient(135deg,#aacdf2 0%,#b9d7f5 45%,#cfe4cf 60%,#aacdf2 100%)}
.fcol{top:4333px;color:var(--white)}
.fcol h6{font-size:19px;font-weight:700;margin-bottom:26px}
.fcol ul{list-style:none;font-size:12.5px;line-height:26.5px;color:#e3e3e3}
.contact-item{display:flex;gap:10px;font-size:12.5px;line-height:18px;color:#e3e3e3;margin-bottom:18px}
.fcol p{font-size:12.5px;line-height:18px;color:#e3e3e3;width:260px}
.email-field{margin-top:22px;width:248px;height:46px;background:var(--white);display:flex;align-items:center;justify-content:space-between;padding:0 16px;font-size:12px;color:#888}
.socials{left:916px;top:4380px;display:flex;gap:11px}
.socials span{width:41px;height:41px;border-radius:50%;border:1px solid #666;background:#3a3a3a}
.footline{left:90px;top:4600px;width:1020px;height:1px;background:#4a4a4a}
.copy{left:0;width:1200px;top:4632px;text-align:center;font-size:11.5px;font-weight:600;color:var(--white)}
.to-top{left:1130px;top:4598px;width:42px;height:42px;border-radius:50%;background:var(--red);display:flex;align-items:center;justify-content:center}
</style>
</head>
<body>

<header>
  <a class="abs brand" href="#"><span class="brand-mark"></span>Brindle Staffing</a>
  <nav class="abs nav">
    <a class="active" href="#">HOME</a>
    <a class="drop" href="#">ABOUT</a>
    <a class="drop" href="#">SERVICES</a>
    <a class="drop" href="#">ARTICLES</a>
    <a class="drop" href="#">TRAINING</a>
    <a href="#">CONTACT US</a>
  </nav>
</header>

<h1 class="abs hero-title">Recruiting and placing skilled <span class="hl">Philippine</span> workers into UK companies</h1>
<div class="abs stats">
  <div class="stat"><b>357+</b><span>People<br>Recruited</span></div>
  <div class="stat"><b>100+</b><span>Happy<br>Clients</span></div>
  <div class="stat"><b>15+</b><span>Our<br>Countries</span></div>
</div>
<svg class="abs scroll-arrow" width="30" height="40" viewBox="0 0 30 40"><path d="M15 2v34M3 24l12 12 12-12" fill="none" stroke="#222" stroke-width="1.8"/></svg>

<div class="abs photo photo-engineer" role="img" aria-label="Female engineer in hard hat and safety glasses beside industrial robot arm"></div>
<div class="abs photo-engineer-low" role="img" aria-label="Continuation of engineer photograph"></div>
<div class="abs outline-clip" style="left:89px;top:760px;width:616px;height:264px">
  <div class="outline" style="font-size:290px;margin-top:-20px;margin-left:-12px">Philippine</div>
</div>
<div class="abs photo-weld" role="img" aria-label="Welder at work with bright sparks"></div>
<svg class="abs" style="left:918px;top:1121px" width="64" height="64" viewBox="0 0 64 64"><circle cx="32" cy="32" r="31" fill="none" stroke="#fff" stroke-width="2"/><path d="M26 21l17 11-17 11z" fill="#fff"/></svg>

<div class="abs eyebrow">Introduction</div>
<h2 class="abs intro-title">What the business<br>is about BS</h2>
<p class="abs intro-text">We source skilled workers directly from the Philippines to work in the UK. With offices , training locations and specialist recruiters we can find the highest quality individuals to add value and resources to any UK business. We delivery quality based on vast experience over a number of years.</p>
<a class="abs more" style="left:180px;top:1405px" href="#">READ MORE</a>

<a class="abs svc red" style="left:225px" href="#">
  <svg width="66" height="66" viewBox="0 0 66 66" fill="none" stroke="#fff" stroke-width="2"><rect x="8" y="30" width="42" height="24" rx="2"/><circle cx="29" cy="18" r="8"/><path d="M21 30v-3a8 8 0 0116 0v3M22 60h14M48 14l6-6M52 22h8"/></svg>
  <h3>Engineer<br>Services</h3>
  <svg class="go" width="22" height="14" viewBox="0 0 22 14" fill="none" stroke="#fff" stroke-width="1.5"><path d="M1 7h19M14 1l6 6-6 6"/></svg>
</a>
<a class="abs svc orange" style="left:482px" href="#">
  <svg width="66" height="66" viewBox="0 0 66 66" fill="none" stroke="#fff" stroke-width="2"><circle cx="33" cy="16" r="8"/><circle cx="16" cy="28" r="6"/><circle cx="50" cy="28" r="6"/><path d="M19 56V40a14 14 0 0128 0v16M5 56V46a10 10 0 0114-9M61 56V46a10 10 0 00-14-9"/></svg>
  <h3>Health<br>workers</h3>
  <svg class="go" width="22" height="14" viewBox="0 0 22 14" fill="none" stroke="#fff" stroke-width="1.5"><path d="M1 7h19M14 1l6 6-6 6"/></svg>
</a>
<a class="abs svc red" style="left:740px" href="#">
  <svg width="66" height="66" viewBox="0 0 66 66" fill="none" stroke="#fff" stroke-width="2"><rect x="20" y="6" width="26" height="28" rx="10"/><rect x="26" y="16" width="14" height="8"/><path d="M14 60V46a12 12 0 0112-12h14a12 12 0 0112 12v14M8 12l4 8M4 20l8 0"/></svg>
  <h3>Welders<br>Services</h3>
  <svg class="go" width="22" height="14" viewBox="0 0 22 14" fill="none" stroke="#fff" stroke-width="1.5"><path d="M1 7h19M14 1l6 6-6 6"/></svg>
</a>
<a class="abs more" style="left:536px;top:1870px;font-size:11.5px" href="#">VIEW ALL SERVICES</a>

<div class="abs photo-training" role="img" aria-label="Two smiling workers in hard hats and work uniforms"></div>
<div class="abs outline-clip" style="left:0;top:2300px;width:1200px;height:264px">
  <div class="outline" style="font-size:290px;margin-top:0;margin-left:-30px">Training</div>
</div>

<h2 class="abs lead">Recruiting and placing skilled <span class="hl">Philippine</span> workers into UK companies ETC...</h2>
<div class="abs row" style="top:2674px;height:132px"><h4>UK Skilled<br>Workers List</h4><p>The UK government since brexit have developed a new system based on points (similar to Australia) when recruiting from outside of the UK. Previuosly EU citizens could work in...</p></div>
<div class="abs row" style="top:2838px;height:135px"><h4>Sponsor<br>Licence</h4><p>If you have areas of your business that meet the entry requirements of skilled labour your next step is to gain a sponsor licence for your business. There are different types of licences...</p></div>
<div class="abs row" style="top:3004px;height:100px;border:0"><h4>Recruitment<br>Timeline</h4><p>Our teams in the Philippines source suitable candidates, documentation required for each candidate will be checked and vetted by the Recruitment Team. Once deemed qualified,...</p></div>

<h2 class="abs section-title">Latest Articles</h2>
<article class="abs card" style="left:145px">
  <div class="card-img" role="img" aria-label="Worker in orange hard hat and high-visibility vest" style="background:linear-gradient(135deg,#5b6470,#e38a3a)"></div>
  <div class="card-body"><div class="card-date">25-05-2022</div><h5>Some heading goes here</h5><p>Aenean sollicitudin lorem quis nisi elit consequat ipsum nec...</p></div>
</article>
<article class="abs card" style="left:451px">
  <div class="card-img" role="img" aria-label="Smiling worker in yellow hard hat in a factory" style="background:linear-gradient(135deg,#6e7782,#2f3a48 60%,#d9b23a)"></div>
  <div class="card-body"><div class="card-date">25-05-2022</div><h5>Some heading goes here</h5><p>Aenean sollicitudin lorem quis nisi elit consequat ipsum nec...</p></div>
</article>
<article class="abs card" style="left:760px">
  <div class="card-img" role="img" aria-label="Welder in protective mask with sparks" style="background:linear-gradient(135deg,#2a3a5a,#c4782f 70%,#5a3a20)"></div>
  <div class="card-body"><div class="card-date">25-05-2022</div><h5>Some heading goes here</h5><p>Aenean sollicitudin lorem quis nisi elit consequat ipsum nec...</p></div>
</article>

<div class="abs outline-clip" style="left:0;top:3700px;width:1200px;height:220px">
  <div class="outline faint" style="font-size:260px;margin-top:-30px;margin-left:-10px">Philippine</div>
</div>

<footer>
  <div class="abs footer"></div>
  <div class="abs map" role="img" aria-label="Map of the Philippines and surrounding seas"></div>

  <div class="abs fcol" style="left:125px">
    <h6>Quick links</h6>
    <ul><li>Home</li><li>About</li><li>Services</li><li>Articles</li><li>Training</li><li>Contact us</li></ul>
  </div>
  <div class="abs fcol" style="left:313px">
    <h6>Contact info</h6>
    <div class="contact-item"><svg width="12" height="12" viewBox="0 0 12 12"><rect x="0.5" y="2" width="11" height="8" fill="#eb3d1f"/><path d="M1 2.5l5 4 5-4" stroke="#2f2f2f" fill="none"/></svg><span>Email:<br>sales@brindlestaffing.example.com</span></div>
    <div class="contact-item"><svg width="12" height="12" viewBox="0 0 12 12"><path d="M2 1l3 .5 1 3-1.5 1a7 7 0 003 3l1-1.5 3 1 .5 3C6 12 0 6 2 1z" fill="#eb3d1f"/></svg><span>Phone:<br>07700900412</span></div>
    <div class="contact-item"><svg width="12" height="14" viewBox="0 0 12 14"><path d="M6 0a5 5 0 015 5c0 4-5 9-5 9S1 9 1 5a5 5 0 015-5z" fill="#eb3d1f"/><circle cx="6" cy="5" r="2" fill="#2f2f2f"/></svg><span>Location:<br>Maple Court, Ashby,<br>Ashby AB1 2CD United Kingdom</span></div>
  </div>
  <div class="abs fcol" style="left:600px">
    <h6>Newsletter</h6>
    <p>Join our mailing list to learn about our latest projects and product offerings</p>
    <div class="email-field"><span>✉&nbsp; Enter your email...</span><svg width="16" height="16" viewBox="0 0 16 16"><path d="M1 8l14-6-5 13-2-5z" fill="#eb3d1f"/></svg></div>
  </div>
  <div class="abs socials"><span></span><span></span><span></span><span></span></div>
  <div class="abs footline"></div>
  <div class="abs copy">© 2023 &nbsp;All Rights Reserved &nbsp;| &nbsp;Brindle Staffing Ltd</div>
  <a class="abs to-top" href="#"><svg width="12" height="14" viewBox="0 0 12 14" fill="none" stroke="#fff" stroke-width="1.6"><path d="M6 13V2M1 6l5-5 5 5"/></svg></a>
</footer>

</body>
</html>
```